NEW Modern Sleek Business Card for VR Language Startup

Our startup is using VR to lead the next wave of world language education. We need a two-sided business card that introduces the larger organization (Quorvel Language Inc) and our contact info on one side and shows the product, Lumidrasca, on the other side.

Side 1 (contact info)= Quorvel Logo and Contact info (name, title, phone, email)

Side 2 (product)= Lumidrasc logo, text, and website
Text= Culturally Immersive Language Learning Games
Website= www.lumidrasc.example

Target Market(s)

Education, Technology

Contact Information for Business Card

Contact info will be updated upon approval of the design. For now, put this as a placeholder.

Perry Hollins
Founder & CEO
phollins@mailtrove.example
(555)-014-2736

Font styles to use
Other font styles liked:
• Gibson and Century Gothic are the brand fonts

Requirements
Nice to have
• I would love to see cohesion between the design and colors of the two logos. I have attached a few business card designs that I like, so you can get a feel for my preferred style.

```html
<!DOCTYPE html>
<html lang="en">
<head>
<meta charset="utf-8">
<title>Quorvel Language – Business Card</title>
<link href="https://fonts.googleapis.com/css2?family=Lato:wght@400;700&display=swap" rel="stylesheet">
<style>
  :root {
    --backdrop: #9c5a2a;
    --card: #1d1d1e;
    --card-back: #1f1f20;
    --white: #ffffff;
    --soft-text: #d6d6d6;
    --rule: #5a5a5a;
    --brand-dot: #ef4a68;
    --product-dot: #4c8ff6;
    --product-name: #4c8ff6;
    --link: #3cb6ef;
    --name-start: #f0813a;
    --name-end: #8a6cf0;
  }
  * { box-sizing: border-box; margin: 0; padding: 0; }
  html, body { width: 1200px; height: 900px; overflow: hidden; }
  body {
    position: relative;
    background: var(--backdrop);
    font-family: "Lato", sans-serif;
  }
  .card {
    position: absolute;
    width: 556px;
    height: 343px;
    box-shadow: 0 4px 10px rgba(0,0,0,.45);
  }
  .card--front { left: 330px; top: 90px; background: var(--card); }
  .card--back { left: 331px; top: 470px; background: var(--card-back); }

  /* front */
  .brand {
    position: absolute;
    top: 78px; left: 0; right: 0;
    display: flex; align-items: center; justify-content: center; gap: 22px;
  }
  .brand__dot { width: 86px; height: 86px; border-radius: 50%; background: var(--brand-dot); }
  .brand__name { color: var(--white); font-weight: 400; text-align: center; line-height: 1; }
  .brand__name-main { display: block; font-size: 44px; letter-spacing: 6px; }
  .brand__name-sub { display: block; font-size: 21px; letter-spacing: 7px; margin-top: 12px; }

  .contact {
    position: absolute;
    top: 243px; left: 0; right: 0;
    display: flex; justify-content: center; align-items: center;
  }
  .contact__person { text-align: right; padding-right: 18px; }
  .contact__name {
    font-size: 20px; font-weight: 700; letter-spacing: .3px;
    background: linear-gradient(90deg, var(--name-start), var(--name-end));
    -webkit-background-clip: text; background-clip: text; color: transparent;
  }
  .contact__title { font-size: 14px; color: var(--white); margin-top: 2px; }
  .contact__divider { width: 1px; height: 42px; background: var(--rule); }
  .contact__details { padding-left: 16px; color: var(--white); font-size: 15px; }
  .contact__line { display: flex; align-items: center; gap: 5px; line-height: 21px; }
  .contact__icon { width: 13px; height: 13px; }

  /* back */
  .product {
    position: absolute; top: 52px; left: 0; right: 0;
    display: flex; flex-direction: column; align-items: center;
  }
  .product__dot { width: 120px; height: 120px; border-radius: 50%; background: var(--product-dot); }
  .product__name {
    margin-top: 22px; font-size: 40px; font-weight: 700;
    color: var(--product-name); letter-spacing: .5px; line-height: 1;
  }
  .tagline {
    position: absolute; top: 268px; left: 0; right: 0;
    text-align: center; color: var(--soft-text); font-size: 15px; letter-spacing: .4px;
  }
  .website {
    position: absolute; top: 296px; left: 60px; right: 60px;
    display: flex; align-items: center; gap: 10px;
  }
  .website__rule { flex: 1; height: 1px; background: var(--rule); }
  .website__url { color: var(--link); font-size: 16px; }
</style>
</head>
<body>
  <section class="card card--front" aria-label="Business card front">
    <div class="brand">
      <div class="brand__dot"></div>
      <div class="brand__name">
        <span class="brand__name-main">QUORVEL</span>
        <span class="brand__name-sub">LANGUAGE</span>
      </div>
    </div>
    <div class="contact">
      <div class="contact__person">
        <div class="contact__name">PERRY HOLLINS</div>
        <div class="contact__title">Founder &amp; CEO</div>
      </div>
      <div class="contact__divider"></div>
      <div class="contact__details">
        <div class="contact__line">
          <svg class="contact__icon" viewBox="0 0 16 16" aria-hidden="true"><path fill="#f08a50" d="M1 6c0-2 3-4 7-4s7 2 7 4l-3 1-1-2H5L4 7 1 6zm3 2h8l2 6H2l2-6zm4 1.5a2 2 0 1 0 0 4 2 2 0 0 0 0-4z"/></svg>
          <span>(555)-014-2736</span>
        </div>
        <div class="contact__line">
          <svg class="contact__icon" viewBox="0 0 16 16" aria-hidden="true"><rect x="1" y="3" width="14" height="10" fill="#8a6cf0"/><path d="M1 3l7 6 7-6" fill="none" stroke="#f08a50" stroke-width="1.4"/></svg>
          <span>phollins@mailtrove.example</span>
        </div>
      </div>
    </div>
  </section>

  <section class="card card--back" aria-label="Business card back">
    <div class="product">
      <div class="product__dot"></div>
      <div class="product__name">Lumidrasc</div>
    </div>
    <p class="tagline">CULTURALLY IMMERSIVE LANGUAGE LEARNING GAMES</p>
    <div class="website">
      <span class="website__rule"></span>
      <span class="website__url">www.lumidrasc.example</span>
      <span class="website__rule"></span>
    </div>
  </section>
</body>
</html>
```